Finish off design for Tool Retailer- One Page Brochure site

We have started work on our tool shop sit but need to to get finished. Just a One page WP that needs tidying up and made to look better and complete.
We also need to be able upload specials and monthly catalogs.
More info in the brief
Target Market(s)
Trades, mines, industiral
Coding
Coded - Design and coding required
Number of Pages Required
1 page
Font styles to use
Sans Serif
Requirements
Must have
- Please see brief
Nice to have
- Please see brief
Should not have
- Please see brief

```html
<!DOCTYPE html>
<html lang="en">
<head>
<meta charset="utf-8">
<title>Ridgeline Tools</title>
<link href="https://fonts.googleapis.com/css2?family=Lato:wght@400;700;900&family=Oswald:wght@600;700&display=swap" rel="stylesheet">
<style>
:root{
  --red:#b5121b;
  --red-dark:#8e0d14;
  --black:#1b1b1b;
  --nav:#222222;
  --grey:#e9e9e9;
  --grey-line:#d6d6d6;
  --text:#333333;
  --muted:#555555;
  --white:#ffffff;
}
*{box-sizing:border-box;margin:0;padding:0}
html,body{width:1200px;height:4215px;overflow:hidden}
body{position:relative;background:var(--white);font-family:'Lato',sans-serif;color:var(--text)}
.abs{position:absolute}
a{color:inherit;text-decoration:none}

/* header */
.topbar{left:0;top:0;width:1200px;height:95px;background:var(--red)}
.brand{left:112px;top:32px;width:250px;color:var(--white);font-weight:900;font-size:22px;line-height:30px;letter-spacing:.5px;display:flex;align-items:center;gap:10px;text-transform:uppercase;white-space:nowrap}
.brand .dot{width:16px;height:16px;background:var(--white);flex:none}
.field-top{top:30px;height:36px;border:1.5px solid #e25a60;border-radius:18px;color:var(--white);font-size:13px;padding:10px 20px;font-weight:700}
.btn-dark{background:var(--black);color:var(--white);border-radius:22px;font-size:13px;font-weight:700;text-align:center}
.navbar{left:0;top:95px;width:1200px;height:60px;background:var(--nav)}
.nav{right:115px;top:115px;display:flex;gap:28px;color:var(--white);font-size:14px;font-weight:700}

/* hero */
.hero{left:0;top:155px;width:1200px;height:520px;background:linear-gradient(100deg,#3a3a3a 0%,#2a2725 45%,#4a1a1c 75%,#2b2b2b 100%)}
.social{left:34px;width:56px;height:56px;border-radius:50%;background:rgba(255,255,255,.85)}
.hero-title{left:242px;top:310px;color:var(--white);font-size:33px;font-weight:700;line-height:44px}
.hero-copy{left:242px;top:410px;width:345px;color:#e6e6e6;font-size:13px;line-height:19px}
.btn-learn{left:242px;top:487px;width:150px;height:36px;line-height:36px}
.dots{left:1076px;top:360px;display:flex;flex-direction:column;gap:20px}
.dots span{width:10px;height:10px;border-radius:50%;background:var(--red)}
.dots span.on{background:var(--white)}

.brandband{left:0;top:590px;width:1200px;height:200px}
.brandnames{left:140px;top:605px;width:930px;display:flex;justify-content:space-between;color:var(--white);font-weight:900;font-size:34px}
.promo{top:670px;height:95px;background:var(--black);color:var(--white);text-align:center;padding-top:18px}
.promo h3{font-family:'Oswald',sans-serif;font-size:31px;font-weight:700;text-transform:uppercase;line-height:36px}
.promo p{font-size:11px;font-weight:700}

/* section heads */
.sec-head{left:112px;height:34px;display:flex;align-items:center}
.sec-head .bar{height:34px;background:#e3e3e3;padding:0 22px;display:flex;align-items:center;font-size:28px;font-weight:900;text-transform:uppercase;color:#222}
.sec-head .slash{width:10px;height:32px;background:#222;transform:skewX(-22deg);margin-left:16px}

/* product cards */
.card{width:308px;border:1px solid var(--grey-line);background:var(--white)}
.card .pic{height:252px}
.card .body{background:var(--grey);height:138px;text-align:center;padding:14px 22px 0}
.card h4{font-size:15px;font-weight:900;text-transform:uppercase;margin-bottom:12px}
.card p{font-size:11.5px;line-height:17px;color:var(--muted)}
.btn-more{left:492px;top:1718px;width:214px;height:36px;line-height:36px}

/* catalogue */
.cat-dark{left:112px;top:1894px;width:487px;height:405px;background:var(--black)}
.cat-name{left:172px;top:1985px;color:var(--white);font-size:38px;font-weight:900;line-height:48px}
.cat-tag{left:158px;top:2150px;color:#e0232c;font-size:22px;font-weight:700;display:flex;align-items:center;gap:14px}
.cat-pic{left:370px;top:1940px;width:190px;height:200px;border-radius:50%}
.cat-card{left:528px;top:1930px;width:557px;height:318px;background:var(--white);box-shadow:0 2px 12px rgba(0,0,0,.15);padding:44px 70px 0 82px}
.cat-card h2{font-size:22px;font-weight:700;margin-bottom:26px;text-transform:uppercase;white-space:nowrap}
.cat-card p{font-size:13.5px;line-height:21px;color:var(--muted);margin-bottom:24px}
.btn-red{background:var(--red);color:var(--white);border-radius:22px;font-size:15px;font-weight:700;text-align:center;display:inline-flex;align-items:center;justify-content:center;gap:10px}

/* about */
.about-h{left:122px;top:2430px;width:470px;font-size:22px;font-weight:900;line-height:32px;text-transform:uppercase;color:#222}
.about-p{left:122px;top:2546px;width:460px;font-size:13.5px;line-height:20px;color:var(--muted)}
.about-pic{left:613px;top:2352px;width:472px;height:385px;background:linear-gradient(135deg,#7d8fa3 0%,#3d4a5c 40%,#b58a4a 75%,#d6a23a 100%)}

/* shop by category */
.tabs{left:436px;top:2806px;width:649px;height:28px;background:var(--red);color:var(--white);font-size:11px;display:flex;align-items:center;justify-content:center;gap:10px}
.tabs span.sep{opacity:.7}
.catcard{top:2875px;width:308px;border:1px solid var(--grey-line)}
.catcard .pic{height:253px}
.catcard .label{height:50px;background:var(--grey);text-align:center;line-height:50px;font-size:15px;font-weight:900;text-transform:uppercase}

/* contact */
.talk-bg{left:599px;top:3260px;width:601px;height:700px;background:linear-gradient(110deg,#f1e4d6 0%,#e8cdb6 40%,#d6a48a 70%,#c7373f 100%)}
.diamond{left:492px;top:3330px;width:220px;height:220px;border:6px solid var(--white);transform:rotate(45deg);background:linear-gradient(180deg,#8fb4d8 0%,#b9c6cf 55%,#6c6a63 100%)}
.talk-h{left:112px;top:3322px;font-size:40px;font-weight:700;color:#111}
.contact{left:122px;top:3420px;font-size:17px;line-height:31px;color:#222}
.contact .row{display:flex;gap:28px}
.contact svg{width:14px;height:14px;margin-top:8px;flex:none}
.input{left:112px;width:416px;height:42px;border:1px solid #cfcfcf;font-size:12px;padding:10px 12px;color:#444}
.btn-submit{left:418px;top:3866px;width:110px;height:40px;line-height:40px;font-size:13px;font-weight:900;display:block}

/* footer */
.footer{left:0;top:3962px;width:1200px;height:253px;background:var(--nav);border-top:5px solid var(--red)}
.foot-brand{left:112px;top:3992px;width:230px;height:84px;background:var(--red);color:var(--white);font-weight:900;font-size:20px;text-transform:uppercase;display:flex;align-items:center;justify-content:center;gap:10px;white-space:nowrap}
.foot-brand .dot{width:14px;height:14px;background:var(--white)}
.fsoc{top:4096px;width:12px;height:12px;border-radius:50%;background:var(--white)}
.copy{left:112px;top:4135px;color:var(--white);font-size:13px}
.foot-h{top:3990px;color:var(--white);font-size:17px}
.links{top:4030px;color:var(--white);font-size:13px;line-height:31px}
.links li{list-style:none;display:flex;align-items:center;gap:22px}
.links li::before{content:"";width:5px;height:5px;border-top:2px solid #fff;border-right:2px solid #fff;transform:rotate(45deg)}
.foot-p{left:792px;top:4038px;color:var(--white);font-size:13px}
.sub-in{left:792px;top:4077px;width:290px;height:40px;background:var(--black);border-radius:20px;color:var(--white);font-size:12px;padding:12px 20px}
.sub-btn{left:1030px;top:4080px;width:50px;height:34px;border-radius:17px;background:var(--red)}
.totop{left:1140px;top:4160px;color:var(--white);font-size:11px}
</style>
</head>
<body>

<!-- header -->
<div class="abs topbar"></div>
<div class="abs brand"><span class="dot"></span>Ridgeline Tools</div>
<div class="abs field-top" style="left:380px;width:252px">ENTER YOUR NAME</div>
<div class="abs field-top" style="left:652px;width:250px">EMAIL ID</div>
<div class="abs btn-dark" style="left:908px;top:28px;width:178px;height:40px;line-height:40px">NEWSLETTER SIGN UP</div>
<div class="abs navbar"></div>
<nav class="abs nav"><a>HOME</a><a>ABOUT</a><a>SPECIALS</a><a>CONTACT US</a><a>CURRENT CATALOGUE</a></nav>

<!-- hero -->
<div class="abs hero" role="img" aria-label="Dark workshop photo with red cordless drills, hammer, wrench and utility knife on wooden boards"></div>
<div class="abs social" style="top:228px"></div>
<div class="abs social" style="top:307px"></div>
<div class="abs social" style="top:386px"></div>
<div class="abs social" style="top:465px"></div>
<h1 class="abs hero-title">ALL TOOLS<br>FOR ANY OCCASION</h1>
<p class="abs hero-copy">Content of this page comes here. Content of this page comes here. Content of this page comes here. Content of this page comes here.</p>
<a class="abs btn-dark btn-learn">LEARN MORE &nbsp;›</a>
<div class="abs dots"><span></span><span class="on"></span><span></span></div>

<svg class="abs brandband" width="1200" height="200" viewBox="0 0 1200 200">
  <polygon points="0,20 1200,0 1200,80 110,80 0,200" fill="#b5121b"/>
</svg>
<div class="abs brandnames"><span>KORVAN</span><span>TESSARO</span><span>BRANNOCK</span><span>HALVORN</span><span>VELTRIX</span></div>

<div class="abs promo" style="left:112px;width:321px"><h3>Redemption Offers</h3><p>Major Brands Offers</p></div>
<div class="abs promo" style="left:444px;width:315px"><h3>Catalogue Special</h3><p>Catalogue Special</p></div>
<div class="abs promo" style="left:767px;width:318px"><h3>Clearance Stock</h3><p>Prices as Marked, Limited Time Only</p></div>

<!-- current specials -->
<div class="abs sec-head" style="top:808px"><div class="bar">Current Specials</div><div class="slash"></div></div>

<div class="abs card" style="left:112px;top:866px"><div class="pic" role="img" aria-label="Orange leaf blower" style="background:radial-gradient(circle,#e8632c 0%,#f6d4c4 45%,#fff 70%)"></div><div class="body"><h4>Automotive</h4><p>Lorem ipsum dolor sit amet, consectetur adipiscing elit, sed do eiusmod tempor incididunt ut labore et dolore magna aliqua.</p></div></div>
<div class="abs card" style="left:447px;top:866px"><div class="pic" role="img" aria-label="Green snow blower" style="background:radial-gradient(circle,#6ed12b 0%,#d7f2c2 45%,#fff 70%)"></div><div class="body"><h4>Lawn Mowers</h4><p>Lorem ipsum dolor sit amet, consectetur adipiscing elit, sed do eiusmod tempor incididunt ut labore et dolore magna aliqua.</p></div></div>
<div class="abs card" style="left:778px;top:866px"><div class="pic" role="img" aria-label="Red air compressor" style="background:radial-gradient(circle,#8a1c22 0%,#e3c3c5 45%,#fff 70%)"></div><div class="body"><h4>Air Tools + Compressors</h4><p>Lorem ipsum dolor sit amet, consectetur adipiscing elit, sed do eiusmod tempor incididunt ut labore et dolore magna aliqua.</p></div></div>

<div class="abs card" style="left:112px;top:1287px"><div class="pic" role="img" aria-label="Red push lawn mower" style="background:radial-gradient(circle,#c8262c 0%,#eec9ca 45%,#fff 70%)"></div><div class="body"><h4>Hand Tool</h4><p>Lorem ipsum dolor sit amet, consectetur adipiscing elit, sed do eiusmod tempor incididunt ut labore et dolore magna aliqua.</p></div></div>
<div class="abs card" style="left:447px;top:1287px"><div class="pic" role="img" aria-label="Pair of red and black cordless drills" style="background:radial-gradient(circle,#5a2a2c 0%,#e0cfd0 45%,#fff 70%)"></div><div class="body"><h4>Hnad Power Tool</h4><p>Lorem ipsum dolor sit amet, consectetur adipiscing elit, sed do eiusmod tempor incididunt ut labore et dolore magna aliqua.</p></div></div>
<div class="abs card" style="left:778px;top:1287px"><div class="pic" role="img" aria-label="Yellow and black drill kit with bag" style="background:radial-gradient(circle,#e2b320 0%,#f4e6bb 45%,#fff 70%)"></div><div class="body"><h4>Halvorn Hand Tools</h4><p>Lorem ipsum dolor sit amet, consectetur adipiscing elit, sed do eiusmod tempor incididunt ut labore et dolore magna aliqua.</p></div></div>

<a class="abs btn-dark btn-more">VIEW MORE PRODUCTS &nbsp;›</a>

<!-- latest catalogue -->
<div class="abs sec-head" style="top:1834px"><div class="bar">Latest Catalogue</div><div class="slash"></div></div>
<div class="abs cat-dark"></div>
<div class="abs cat-pic" role="img" aria-label="Green circular saw" style="background:radial-gradient(circle,#5fbf3a 0%,#2b4d24 55%,#1b1b1b 72%)"></div>
<div class="abs cat-name">Ridgeline<br>Tools</div>
<div class="abs cat-tag"><svg width="18" height="18" viewBox="0 0 18 18"><path d="M12 2 L5 9 L12 16" stroke="#e0232c" stroke-width="3" fill="none"/></svg>Just a little idea</div>
<div class="abs cat-card">
  <h2>Finibus Bonorum et Malorum</h2>
  <p>Sed ut perspiciatis unde omnis iste natus error sit voluptatem accusantium doloremque laudantium, totam rem aperiam, eaque ipsa quae ab illo inventore veritatis et quasi architecto beatae vitae dicta sunt explicabo. Nemo enim ipsam voluptatem quia voluptas sit aspernatur aut odit aut fugit.</p>
  <a class="btn-red" style="width:230px;height:40px">Download Catalogue
    <svg width="14" height="14" viewBox="0 0 14 14"><path d="M7 1v8M3 6l4 4 4-4M2 13h10" stroke="#fff" stroke-width="2" fill="none"/></svg></a>
</div>

<!-- about -->
<div class="abs sec-head" style="top:2359px"><div class="bar">About Us</div><div class="slash"></div></div>
<h2 class="abs about-h">Our company started out with an idea to supply and meet the everyday tool needs of people.</h2>
<p class="abs about-p">Sed ut perspiciatis unde omnis iste natus error sit voluptatem accusantium doloremque laudantium, totam rem aperiam, eaque ipsa quae ab illo inventore veritatis et quasi architecto beatae vitae dicta sunt explicabo. Nemo enim ipsam voluptatem quia voluptas sit aspernatur aut odit aut fugit, ere.</p>
<a class="abs btn-red" style="left:122px;top:2662px;width:146px;height:40px">Read more ›</a>
<div class="abs about-pic" role="img" aria-label="Tradesperson with a tool belt holding a cordless drill"></div>

<!-- shop by category -->
<div class="abs sec-head" style="top:2804px"><div class="bar">Shop by Category</div><div class="slash"></div></div>
<div class="abs tabs"><span>Air Tools + Compressors</span><span class="sep">|</span><span>Automotive</span><span class="sep">|</span><span>Lawn Mowers</span><span class="sep">|</span><span>New Arrivals</span><span class="sep">|</span><span>Popular</span><span class="sep">|</span><span>Power Tools</span><span class="sep">|</span><span>Uncategorized</span></div>
<div class="abs catcard" style="left:112px"><div class="pic" role="img" aria-label="Orange leaf blower" style="background:radial-gradient(circle,#e8632c 0%,#f6d4c4 45%,#fff 70%)"></div><div class="label">Automotive</div></div>
<div class="abs catcard" style="left:447px"><div class="pic" role="img" aria-label="Green snow blower" style="background:radial-gradient(circle,#6ed12b 0%,#d7f2c2 45%,#fff 70%)"></div><div class="label">Lawn Mowers</div></div>
<div class="abs catcard" style="left:778px"><div class="pic" role="img" aria-label="Red air compressor" style="background:radial-gradient(circle,#8a1c22 0%,#e3c3c5 45%,#fff 70%)"></div><div class="label"></div></div>

<!-- contact -->
<div class="abs talk-bg" role="img" aria-label="Woman hammering a nail to hang picture frames on a wall"></div>
<div class="abs diamond" role="img" aria-label="Storefront of the tool shop"></div>
<h2 class="abs talk-h">LET'S TALK</h2>
<div class="abs contact">
  <div class="row"><svg viewBox="0 0 14 14"><path d="M7 0a5 5 0 0 0-5 5c0 4 5 9 5 9s5-5 5-9a5 5 0 0 0-5-5z" fill="#222"/></svg><span>48 Quarry Lane, Ironbark Street,<br>Unit 3, Emerald</span></div>
  <div class="row"><svg viewBox="0 0 14 14"><path d="M2 1l3 0 1 3-2 1.5c1 2 2.5 3.5 4.5 4.5L10 8l3 1v3c-6 1-12-5-11-11z" fill="#222"/></svg><span>+61 400 218 374<br>+61 400 218 375</span></div>
  <div class="row"><svg viewBox="0 0 14 14"><rect x="0" y="2" width="14" height="10" fill="#222"/><path d="M0 2l7 5 7-5" stroke="#fff" fill="none"/></svg><span>hello@ridgelinetools.example</span></div>
</div>
<div class="abs input" style="top:3622px">Name</div>
<div class="abs input" style="top:3676px">Email</div>
<div class="abs input" style="top:3730px">Phone</div>
<div class="abs input" style="top:3786px;height:70px">Message</div>
<a class="abs btn-red btn-submit">SUBMIT</a>

<!-- footer -->
<div class="abs footer"></div>
<div class="abs foot-brand"><span class="dot"></span>Ridgeline Tools</div>
<div class="abs fsoc" style="left:112px"></div>
<div class="abs fsoc" style="left:140px"></div>
<div class="abs fsoc" style="left:168px"></div>
<div class="abs fsoc" style="left:196px"></div>
<div class="abs fsoc" style="left:224px"></div>
<div class="abs copy">© 2018 &nbsp;| &nbsp;&nbsp;www.ridgelinetools.example</div>
<div class="abs foot-h" style="left:441px">Useful Links</div>
<ul class="abs links" style="left:441px"><li>Home</li><li>Shop</li><li>Deals</li><li>About Us</li><li>FAQ</li></ul>
<ul class="abs links" style="left:613px"><li>Specials</li><li>Contact Us</li><li>Latest Catalogue</li><li>Categories</li><li>Blog</li></ul>
<div class="abs foot-h" style="left:792px">Subscribe To Our Newsletter</div>
<p class="abs foot-p">You can be always up to date with our company news!</p>
<div class="abs sub-in">Enter Email id</div>
<svg class="abs sub-btn" viewBox="0 0 50 34"><rect width="50" height="34" rx="17" fill="#b5121b"/><path d="M17 17l16-7-5 15-3-6z" fill="#fff"/></svg>
<div class="abs totop">^<br>M3</div>

</body>
</html>
```